Fitness website

Website for a fitness brand (see attached specs). Design needs to be modern and vibrant with CTAs on every page. We will provide logos, images, etc but for now user placeholder text and images. For now use the name 'Veltrano Athletics' as the name to use on the design. The goal of this site is to either get people to join the gym (5 physical locations across the US); buy an online program; buy merch or supplements or sign up for the newsletter. Pleas use images from this foldeR: https://files.quorbex.net/share/8kTq27wLmZr

We will be coding this in ReactNative. Lots more work for the winner as well, this is a 1st project for us.

Target Market(s)

fitness enthusiats

Industry/Entity Type

fitness, health, wellness

Number of Pages Required

5+ page

Font styles to use
Other font styles liked:
• Lato

Colors
0054AA
0677BA
7BADD7
CADEEF
E8F1F8
0094D4
00A9DD
6FCCEA
C7EBF8
E9F6FB
00AB8E
00BBA5
67D7C9
C6EFE9
E9F9F6
EE7325
F08F49
F5BC92
FAE3D3
FDF4ED

Requirements
Must have
• must be reactive. most people will view it first on mobile
Nice to have
• video in hero section of top of home page

```html
<!DOCTYPE html>
<html lang="en">
<head>
<meta charset="utf-8">
<title>Veltrano Athletics</title>
<link href="https://fonts.googleapis.com/css2?family=Lexend:wght@500;600;700&family=Poppins:wght@400;500;600&display=swap" rel="stylesheet">
<style>
:root{
  --green:#17893a;
  --green-dark:#0f6e2c;
  --orange:#ee7325;
  --ink:#1b1b1b;
  --muted:#6d6d6d;
  --line:#eeeeee;
  --footer:#1d1d1d;
  --white:#ffffff;
}
*{box-sizing:border-box;margin:0;padding:0}
html,body{width:1200px;height:5046px;overflow:hidden}
body{position:relative;font-family:"Poppins",sans-serif;color:var(--ink);background:var(--white)}
.abs{position:absolute}
h1,h2,h3,.brand{font-family:"Lexend",sans-serif}
.btn{position:absolute;display:flex;align-items:center;justify-content:center;background:var(--orange);color:var(--white);font-size:13px;font-weight:500;text-transform:uppercase;border-radius:7px;letter-spacing:.2px}
.section-title{position:absolute;left:0;width:1200px;text-align:center;font-size:37px;font-weight:700;text-transform:uppercase;letter-spacing:.5px}
.brand{color:var(--green);font-weight:700;font-size:24px;letter-spacing:.5px;line-height:1.1}
/* hero */
.hero{left:0;top:0;width:1200px;height:675px;background:linear-gradient(100deg,#141414 0%,#2a2a2a 45%,#4a4a4a 65%,#1d1d1d 100%)}
.nav{position:absolute;left:428px;top:37px;display:flex;gap:26px;font-size:13px;color:var(--white)}
.nav .on{color:#3fbf5a}
.nav-icons{position:absolute;left:1040px;top:35px;display:flex;gap:20px}
.hero h1{position:absolute;left:58px;top:204px;font-size:47px;line-height:60px;color:var(--white);text-transform:uppercase;font-weight:700}
.hero p{position:absolute;left:61px;top:400px;width:480px;font-size:15px;line-height:25px;color:var(--white)}
/* train */
.way-card{position:absolute;top:818px;width:226px;height:255px;background:var(--white);border-radius:8px;box-shadow:0 2px 14px rgba(0,0,0,.07);text-align:center}
.way-card svg{margin-top:34px}
.way-card h3{font-size:18px;font-weight:600;margin-top:14px}
.way-card p{font-size:12.5px;line-height:19px;color:var(--muted);padding:10px 26px 0}
/* about */
.about{left:0;top:1220px;width:1200px;height:634px;background:var(--green);color:var(--white)}
.oval{position:absolute;border:5px solid var(--orange);border-radius:130px}
.about h2{position:absolute;left:662px;top:140px;font-size:36px;font-weight:700}
.about p{position:absolute;left:662px;top:196px;width:410px;font-size:12.5px;line-height:19.5px}
.stat{position:absolute;top:352px;text-align:center}
.stat b{display:block;font-family:"Lexend",sans-serif;font-size:30px;font-weight:500}
.stat span{font-size:12px}
/* membership */
.plan{position:absolute;top:2001px;width:275px;height:452px;background:var(--white);border-radius:10px;box-shadow:0 2px 14px rgba(0,0,0,.08);text-align:center}
.plan .photo{height:165px;border-radius:10px 10px 0 0}
.price{position:absolute;left:92px;top:120px;width:90px;height:90px;border-radius:50%;background:var(--green);border:4px solid var(--white);color:var(--white);display:flex;flex-direction:column;align-items:center;justify-content:center}
.price b{font-family:"Lexend",sans-serif;font-size:28px;line-height:30px}
.price span{font-size:12px}
.plan h3{position:absolute;top:230px;width:100%;font-size:19px;font-weight:600}
.plan ul{position:absolute;left:42px;top:268px;list-style:none;text-align:left}
.plan li{font-size:12.5px;color:var(--muted);height:27px;display:flex;align-items:center;gap:12px}
/* testimonials */
.band{left:0;width:1200px;background:linear-gradient(120deg,#127a34 0%,#1a8f3e 45%,#157f37 70%,#0f6e2c 100%)}
.quote{left:282px;top:2714px;width:636px;height:209px;background:var(--white);border-radius:14px;text-align:center}
.quote p{padding:58px 64px 0;font-size:13px;line-height:21px;color:#555}
/* blog */
.post{position:absolute;top:3143px;width:349px;height:397px;background:var(--white);border-radius:8px;box-shadow:0 2px 14px rgba(0,0,0,.08);text-align:center}
.post .photo{height:188px;border-radius:8px 8px 0 0}
.date{position:absolute;left:141px;top:155px;width:66px;height:66px;border-radius:50%;background:var(--green);border:3px solid var(--white);color:var(--white);display:flex;flex-direction:column;align-items:center;justify-content:center}
.date b{font-family:"Lexend",sans-serif;font-size:25px;line-height:26px}
.date span{font-size:11px}
.post h3{position:absolute;top:244px;width:100%;font-size:19px;font-weight:600}
.post p{position:absolute;top:282px;left:26px;right:26px;font-size:12.5px;line-height:21px;color:var(--muted)}
.post a{position:absolute;top:354px;width:100%;left:0;font-size:13px;font-weight:500;color:var(--orange);text-decoration:none}
/* locations */
.loc{position:absolute;top:4084px;width:200px;text-align:center}
.loc .pin{width:44px;height:44px;margin:0 auto;background:var(--green);display:flex;align-items:center;justify-content:center}
.loc h3{font-size:18px;font-weight:600;margin-top:18px}
.loc p{font-size:12.5px;line-height:20px;color:var(--muted);margin-top:4px}
/* footer */
.footer{left:0;top:4730px;width:1200px;height:316px;background:var(--footer);color:var(--white)}
.footer h4{position:absolute;top:54px;font-family:"Lexend",sans-serif;font-size:17px;font-weight:500;color:#3fbf5a}
.footer ul{position:absolute;left:427px;top:90px;list-style:none;font-size:12.5px;line-height:22.5px}
.social{position:absolute;top:121px;width:34px;height:34px;border:2px solid var(--orange);border-radius:50%}
.contact{position:absolute;left:791px;display:flex;align-items:center;gap:14px;font-size:12.5px}
.contact i{width:32px;height:32px;border-radius:50%;background:var(--orange);display:flex;align-items:center;justify-content:center}
.copy{position:absolute;top:280px;width:100%;text-align:center;font-size:12px}
</style>
</head>
<body>

<!-- Hero -->
<section class="abs hero" role="img" aria-label="Athlete training with battle ropes in a dark gym">
  <div class="abs brand" style="left:63px;top:24px;">VELTRANO ATHLETICS</div>
  <nav class="nav"><span class="on">Home</span><span>About Us</span><span>Programs</span><span>Shop</span><span>Members</span><span>Locations</span><span>Blogs</span></nav>
  <div class="nav-icons">
    <svg width="18" height="18" viewBox="0 0 24 24" fill="none" stroke="#fff" stroke-width="2"><circle cx="10" cy="10" r="7"/><path d="M15 15l6 6"/></svg>
    <svg width="18" height="18" viewBox="0 0 24 24" fill="none" stroke="#fff" stroke-width="2"><circle cx="12" cy="8" r="4"/><path d="M4 21c1-5 15-5 16 0"/></svg>
    <svg width="20" height="18" viewBox="0 0 26 24" fill="none" stroke="#fff" stroke-width="2"><path d="M1 2h4l3 13h13l3-9H7"/><circle cx="10" cy="20" r="2"/><circle cx="19" cy="20" r="2"/></svg>
  </div>
  <h1>Unleash your<br>potential with<br>Veltrano Athletics</h1>
  <p>Train with elite coaches, proven programs, and a global community that pushes you to be your best.</p>
  <div class="btn" style="left:61px;top:484px;width:211px;height:37px;">Start your free trial</div>
</section>

<!-- Train your way -->
<h2 class="section-title" style="top:742px;">Train your way</h2>
<div class="way-card" style="left:119px;">
  <svg width="70" height="70" viewBox="0 0 64 64" fill="none" stroke="#17893a" stroke-width="2.5"><rect x="10" y="8" width="44" height="6"/><path d="M32 14v10M20 56h24M32 44v12"/><circle cx="32" cy="34" r="10"/><path d="M14 56V30M50 56V30"/></svg>
  <h3>Functional Fitness</h3>
  <p>Lorem Ipsum has been the industry's standard dummy text ever since the 1500s, when an unknown.</p>
</div>
<div class="way-card" style="left:364px;">
  <svg width="70" height="70" viewBox="0 0 64 64" fill="none" stroke="#17893a" stroke-width="2.5"><path d="M8 20h48M14 14v12M50 14v12"/><circle cx="32" cy="38" r="12" stroke="#ee7325"/><path d="M20 56l8-14M44 56l-8-14"/></svg>
  <h3>Competitive</h3>
  <p>Lorem Ipsum has been the industry's standard dummy text ever since the 1500s, when an unknown.</p>
</div>
<div class="way-card" style="left:609px;">
  <svg width="70" height="70" viewBox="0 0 64 64" fill="none" stroke="#17893a" stroke-width="2.5"><circle cx="32" cy="14" r="7" stroke="#ee7325"/><path d="M6 28h52M10 22v12M54 22v12M26 28v26h12V28"/></svg>
  <h3>Masters</h3>
  <p>Lorem Ipsum has been the industry's standard dummy text ever since the 1500s, when an unknown.</p>
</div>
<div class="way-card" style="left:854px;">
  <svg width="70" height="70" viewBox="0 0 64 64" fill="none" stroke="#17893a" stroke-width="2.5"><rect x="18" y="10" width="20" height="10" rx="3"/><path d="M22 20v34h12V20"/><circle cx="46" cy="36" r="8" stroke="#ee7325"/></svg>
  <h3>Specialty</h3>
  <p>Lorem Ipsum has been the industry's standard dummy text ever since the 1500s, when an unknown.</p>
</div>
<div class="btn" style="left:533px;top:1104px;width:135px;height:39px;">Read more</div>

<!-- About -->
<section class="abs about">
  <svg class="abs" style="left:90px;top:150px" width="420" height="360" fill="none" stroke="rgba(255,255,255,.12)" stroke-width="2"><circle cx="210" cy="180" r="120"/><circle cx="210" cy="180" r="170"/></svg>
  <div class="oval" role="img" aria-label="Athletes lifting barbells in a gym" style="left:76px;top:76px;width:247px;height:333px;background:linear-gradient(160deg,#4a4a4a,#2a2a2a 60%,#5a4a3e);"></div>
  <div class="oval" role="img" aria-label="Athletes holding weight plates overhead" style="left:339px;top:225px;width:246px;height:333px;background:linear-gradient(160deg,#2f3340,#1f2229 55%,#5a4c44);"></div>
  <h2>ABOUT US</h2>
  <p>Lorem Ipsum has been the industry's standard dummy text ever since the 1500s, when an unknown printer took a galley of type and scrambled it to make a type specimen book. It has survived not only five centuries, but also the leap into electronic typesetting, remaining essentially unchanged. It was popularised in the 1960s with the release of Letraset sheets containing Lorem Ipsum passages, and more recently.</p>
  <div class="stat" style="left:670px;"><b>140+</b><span>Expert Coachs</span></div>
  <div class="stat" style="left:782px;"><b>978+</b><span>Members joines</span></div>
  <div class="stat" style="left:902px;"><b>50+</b><span>Fitness Programs</span></div>
  <div class="btn" style="left:662px;top:444px;width:173px;height:39px;">Get started now</div>
</section>

<!-- Membership -->
<h2 class="section-title" style="top:1920px;">Our membership</h2>
<div class="plan" style="left:164px;">
  <div class="photo" role="img" aria-label="Group cycling class" style="background:linear-gradient(160deg,#6b6b6b,#2e2e2e);"></div>
  <div class="price"><b>$30</b><span>Monthly</span></div>
  <h3>Beginner Plan</h3>
  <ul>
    <li><svg width="14" height="12" viewBox="0 0 14 12"><path d="M1 6l4 4 8-9" stroke="#17893a" stroke-width="2.5" fill="none"/></svg>Unlimited Club access</li>
    <li><svg width="14" height="12" viewBox="0 0 14 12"><path d="M1 6l4 4 8-9" stroke="#17893a" stroke-width="2.5" fill="none"/></svg>Groud attendance</li>
    <li><svg width="14" height="12" viewBox="0 0 14 12"><path d="M1 6l4 4 8-9" stroke="#17893a" stroke-width="2.5" fill="none"/></svg>Gym visits</li>
    <li><svg width="14" height="12" viewBox="0 0 14 12"><path d="M1 6l4 4 8-9" stroke="#17893a" stroke-width="2.5" fill="none"/></svg>Visits to the bath complex</li>
  </ul>
  <div class="btn" style="left:70px;top:390px;width:135px;height:41px;">Join now</div>
</div>
<div class="plan" style="left:462px;">
  <div class="photo" role="img" aria-label="Athlete lunging with dumbbells" style="background:linear-gradient(160deg,#555,#1e1e1e);"></div>
  <div class="price"><b>$60</b><span>Monthly</span></div>
  <h3>Premium Plan</h3>
  <ul>
    <li><svg width="14" height="12" viewBox="0 0 14 12"><path d="M1 6l4 4 8-9" stroke="#17893a" stroke-width="2.5" fill="none"/></svg>Unlimited Club access</li>
    <li><svg width="14" height="12" viewBox="0 0 14 12"><path d="M1 6l4 4 8-9" stroke="#17893a" stroke-width="2.5" fill="none"/></svg>Groud attendance</li>
    <li><svg width="14" height="12" viewBox="0 0 14 12"><path d="M1 6l4 4 8-9" stroke="#17893a" stroke-width="2.5" fill="none"/></svg>Gym visits</li>
    <li><svg width="14" height="12" viewBox="0 0 14 12"><path d="M1 6l4 4 8-9" stroke="#17893a" stroke-width="2.5" fill="none"/></svg>Visits to the bath complex</li>
  </ul>
  <div class="btn" style="left:70px;top:390px;width:135px;height:41px;">Join now</div>
</div>
<div class="plan" style="left:760px;">
  <div class="photo" role="img" aria-label="Trainer assisting a client with suspension straps" style="background:linear-gradient(160deg,#8a8a8a,#3a3a3a);"></div>
  <div class="price"><b>$80</b><span>Monthly</span></div>
  <h3>Ultimate Plan</h3>
  <ul>
    <li><svg width="14" height="12" viewBox="0 0 14 12"><path d="M1 6l4 4 8-9" stroke="#17893a" stroke-width="2.5" fill="none"/></svg>Unlimited Club access</li>
    <li><svg width="14" height="12" viewBox="0 0 14 12"><path d="M1 6l4 4 8-9" stroke="#17893a" stroke-width="2.5" fill="none"/></svg>Groud attendance</li>
    <li><svg width="14" height="12" viewBox="0 0 14 12"><path d="M1 6l4 4 8-9" stroke="#17893a" stroke-width="2.5" fill="none"/></svg>Gym visits</li>
    <li><svg width="14" height="12" viewBox="0 0 14 12"><path d="M1 6l4 4 8-9" stroke="#17893a" stroke-width="2.5" fill="none"/></svg>Visits to the bath complex</li>
  </ul>
  <div class="btn" style="left:70px;top:390px;width:135px;height:41px;">Join now</div>
</div>

<!-- Testimonials -->
<section class="abs band" style="top:2534px;height:464px;" role="img" aria-label="Green-tinted gym training scene in the background"></section>
<h2 class="section-title" style="top:2602px;color:var(--white);">What our clients says</h2>
<div class="abs quote">
  <p>Lorem Ipsum has been the industry's standard dummy text ever since the 1500s, when an unknown printer took a galley of type and scrambled it to make a type specimen book. It has survived not only five centuries.</p>
  <div style="margin-top:18px;font-size:14px;font-weight:500;">Client Name</div>
  <div style="font-size:12px;color:var(--muted);margin-top:4px;">fitness training</div>
</div>
<div class="abs" role="img" aria-label="Client portrait" style="left:564px;top:2678px;width:72px;height:72px;border-radius:50%;border:3px solid var(--white);background:linear-gradient(160deg,#8a6a55,#3a2c24);"></div>

<!-- Blog -->
<h2 class="section-title" style="top:3066px;">Latest blog posts</h2>
<div class="post" style="left:61px;">
  <div class="photo" role="img" aria-label="Athlete working with battle ropes" style="background:linear-gradient(160deg,#2b4a6e,#151d2b);"></div>
  <div class="date"><b>01</b><span>march</span></div>
  <h3>Lorem Ipsum Has</h3>
  <p>Lorem Ipsum has been the industry's standard dummy text ever since the 1500s, when an unknown printer took a galley.</p>
  <a href="#">READ MORE</a>
</div>
<div class="post" style="left:425px;">
  <div class="photo" role="img" aria-label="Athlete flexing in a red-lit gym" style="background:linear-gradient(160deg,#8a1d1d,#2a1a1a);"></div>
  <div class="date"><b>07</b><span>Jun</span></div>
  <h3>Lorem Ipsum Has</h3>
  <p>Lorem Ipsum has been the industry's standard dummy text ever since the 1500s, when an unknown printer took a galley.</p>
  <a href="#">READ MORE</a>
</div>
<div class="post" style="left:791px;">
  <div class="photo" role="img" aria-label="Group doing push-ups in a class" style="background:linear-gradient(160deg,#5a6b7d,#2b3340);"></div>
  <div class="date"><b>26</b><span>oct</span></div>
  <h3>Lorem Ipsum Has</h3>
  <p>Lorem Ipsum has been the industry's standard dummy text ever since the 1500s, when an unknown printer took a galley.</p>
  <a href="#">READ MORE</a>
</div>

<!-- Community -->
<section class="abs band" style="top:3615px;height:313px;" role="img" aria-label="Green-tinted workout scene in the background"></section>
<h2 class="section-title" style="top:3684px;color:var(--white);line-height:47px;">Join the ultra<br>community</h2>
<div class="abs" style="left:347px;top:3810px;width:323px;height:42px;border:1px solid rgba(255,255,255,.6);border-radius:6px;background:rgba(255,255,255,.15);color:var(--white);font-size:12px;padding:13px 16px;">Enter Email Address</div>
<div class="btn" style="left:681px;top:3810px;width:171px;height:42px;">Get started now</div>

<!-- Locations -->
<h2 class="section-title" style="top:3994px;">Veltrano location</h2>
<div class="loc" style="left:62px;"><div class="pin"><svg width="18" height="22" viewBox="0 0 18 22"><path d="M9 21s7-7 7-12A7 7 0 0 0 2 9c0 5 7 12 7 12z" fill="#fff"/><circle cx="9" cy="9" r="2.5" fill="#17893a"/></svg></div><h3>Veltrano Athletics</h3><p>Lorem Ipsum has been the industry's standard dummy</p></div>
<div class="loc" style="left:282px;"><div class="pin"><svg width="18" height="22" viewBox="0 0 18 22"><path d="M9 21s7-7 7-12A7 7 0 0 0 2 9c0 5 7 12 7 12z" fill="#fff"/><circle cx="9" cy="9" r="2.5" fill="#17893a"/></svg></div><h3>Veltrano Athletics</h3><p>Lorem Ipsum has been the industry's standard dummy</p></div>
<div class="loc" style="left:500px;"><div class="pin"><svg width="18" height="22" viewBox="0 0 18 22"><path d="M9 21s7-7 7-12A7 7 0 0 0 2 9c0 5 7 12 7 12z" fill="#fff"/><circle cx="9" cy="9" r="2.5" fill="#17893a"/></svg></div><h3>Veltrano Athletics</h3><p>Lorem Ipsum has been the industry's standard dummy</p></div>
<div class="loc" style="left:718px;"><div class="pin"><svg width="18" height="22" viewBox="0 0 18 22"><path d="M9 21s7-7 7-12A7 7 0 0 0 2 9c0 5 7 12 7 12z" fill="#fff"/><circle cx="9" cy="9" r="2.5" fill="#17893a"/></svg></div><h3>Veltrano Athletics</h3><p>Lorem Ipsum has been the industry's standard dummy</p></div>
<div class="loc" style="left:938px;"><div class="pin"><svg width="18" height="22" viewBox="0 0 18 22"><path d="M9 21s7-7 7-12A7 7 0 0 0 2 9c0 5 7 12 7 12z" fill="#fff"/><circle cx="9" cy="9" r="2.5" fill="#17893a"/></svg></div><h3>Veltrano Athletics</h3><p>Lorem Ipsum has been the industry's standard dummy</p></div>
<div class="abs" role="img" aria-label="Outline map of the United States with five location pins" style="left:303px;top:4255px;width:597px;height:401px;border-radius:12px;background:linear-gradient(160deg,#f4f4f4,#e6e6e6);"></div>

<!-- Footer -->
<footer class="abs footer">
  <div class="abs brand" style="left:63px;top:50px;">VELTRANO ATHLETICS</div>
  <div class="social" style="left:80px;"></div>
  <div class="social" style="left:121px;"></div>
  <div class="social" style="left:162px;"></div>
  <h4 style="left:427px;">Navigation</h4>
  <ul><li>Home</li><li>About Us</li><li>Program</li><li>Shop</li><li>Members</li><li>Location</li><li>Blogs</li></ul>
  <h4 style="left:791px;">Contact Us</h4>
  <div class="contact" style="top:92px;"><i><svg width="14" height="14" viewBox="0 0 24 24"><path d="M5 2h4l2 5-3 2a12 12 0 0 0 7 7l2-3 5 2v4a2 2 0 0 1-2 2A19 19 0 0 1 3 4a2 2 0 0 1 2-2z" fill="#fff"/></svg></i>+ 0123 555 014</div>
  <div class="contact" style="top:138px;"><i><svg width="14" height="12" viewBox="0 0 24 18"><rect x="1" y="1" width="22" height="16" rx="2" fill="#fff"/><path d="M2 2l10 8 10-8" stroke="#ee7325" stroke-width="2" fill="none"/></svg></i>info@veltranoathletics.com</div>
  <div class="contact" style="top:184px;"><i><svg width="12" height="15" viewBox="0 0 18 22"><path d="M9 21s7-7 7-12A7 7 0 0 0 2 9c0 5 7 12 7 12z" fill="#fff"/></svg></i>Veltrano athletics...</div>
  <div class="copy">© 2025 Veltrano Athletics. All rights reserved.</div>
</footer>

</body>
</html>
```